salami paper bag design The size is 10.5cm 21.5cm 6.7cm

This time we need to make renew salami package design. Planning to make paper salami package. I tried to design but I couldnt formyself.
So please correct my design and recreate more nicer package design from my salami design that attach on the documents.
Logo part I am planning gold stamp. If anybody can make more nicer logo for the package,I don’t mind it.please change the color and shape and everything.
The size is 10.5cm 21.5cm 6.7cm
Thank you.

Target Market(s)

uper market make costomer feel luxurious

Industry/Entity Type

salami matured meat products

Font styles to use
Sans Serif
Decorative
Script

Colors

Designer to choose colors to be used in the design.

Requirements
Nice to have
• Make customer feel joy for genuine fermented salami with wine
Should not have
• My projrct must not have cheap discount design.

```html
<!DOCTYPE html>
<html lang="en">
<head>
<meta charset="utf-8">
<title>Varenna Handmade Salami – Box Dieline</title>
<link rel="stylesheet" href="https://fonts.googleapis.com/css2?family=Montserrat:wght@700;800&display=swap">
<style>
  :root {
    --backdrop: #e8e8ea;
    --box-purple: #6b3f9c;
    --lavender: #b3a4d3;
    --tab-text: #e4ddf6;
    --accent-red: #e8505b;
    --label-blue: #cfe0ee;
    --pattern-blue: #2f64a0;
    --pattern-violet: #7a4fb8;
    --salami-light: #f1efec;
    --salami-dark: #b89a86;
  }
  html, body {
    margin: 0;
    width: 1200px;
    height: 1200px;
    overflow: hidden;
    background: var(--backdrop);
  }
  .dieline {
    position: absolute;
    left: 220px;
    top: 30px;
    width: 760px;
    height: 1140px;
    display: block;
  }
  .panel { fill: var(--box-purple); }
  .upper-lavender { fill: var(--lavender); }
  .red-rule { fill: none; stroke: var(--accent-red); stroke-width: 4; }
  .tagline-tab { fill: var(--box-purple); }
  .tagline {
    font-family: "Montserrat", sans-serif;
    font-weight: 800;
    font-size: 26px;
    letter-spacing: 1.5px;
    fill: var(--tab-text);
  }
  .brand-disc { fill: var(--lavender); stroke: var(--accent-red); stroke-width: 4; }
  .brand-name {
    font-family: "Montserrat", sans-serif;
    font-weight: 800;
    font-size: 42px;
    fill: #1b1420;
  }
  .brand-dot { fill: none; stroke: #1b1420; stroke-width: 3; }
  .flap-name {
    font-family: "Montserrat", sans-serif;
    font-weight: 800;
    font-size: 30px;
    fill: #1b1420;
  }
  .window { stroke: var(--accent-red); stroke-width: 4; }
  .product-label-back { fill: var(--accent-red); }
  .product-label-front { fill: var(--label-blue); }
  .product-label {
    font-family: "Montserrat", sans-serif;
    font-weight: 800;
    font-size: 25px;
    letter-spacing: 1px;
    fill: var(--accent-red);
  }
</style>
</head>
<body>
<svg class="dieline" viewBox="106 83 701 1052" xmlns="http://www.w3.org/2000/svg">
  <defs>
    <linearGradient id="patternTone" x1="0" y1="0" x2="1" y2="1">
      <stop offset="0" stop-color="var(--pattern-blue)"/>
      <stop offset="0.5" stop-color="var(--pattern-violet)"/>
      <stop offset="1" stop-color="var(--pattern-blue)"/>
    </linearGradient>
    <linearGradient id="salamiTone" x1="0" y1="0" x2="1" y2="1">
      <stop offset="0" stop-color="var(--salami-light)"/>
      <stop offset="0.6" stop-color="#e6e0da"/>
      <stop offset="1" stop-color="var(--salami-dark)"/>
    </linearGradient>
  </defs>

  <!-- top tuck flap -->
  <rect class="panel" x="305" y="83" width="305" height="200"/>
  <g transform="translate(457 183) rotate(90)">
    <circle class="brand-dot" cx="-72" cy="0" r="7"/>
    <text class="flap-name" x="14" y="11" text-anchor="middle">Varenna</text>
  </g>

  <!-- main wrap: side, front, side -->
  <rect class="panel" x="106" y="283" width="701" height="654"/>

  <!-- decorative swirl band -->
  <path role="img" aria-label="Blue and violet swirl pattern band"
        fill="url(#patternTone)"
        d="M106,283 H807 V598 C740,588 680,592 610,612 H305 C235,592 170,588 106,598 Z"/>

  <!-- lavender V header -->
  <path class="upper-lavender" d="M106,283 H807 L610,440 H305 Z"/>
  <path class="red-rule" d="M106,283 L305,440 H610 L807,283"/>

  <!-- tagline tab -->
  <path class="tagline-tab" d="M380,283 H535 V377 Q535,402 510,402 H405 Q380,402 380,377 Z"/>
  <text class="tagline" x="457.5" y="318" text-anchor="middle">LIVING</text>
  <text class="tagline" x="457.5" y="351" text-anchor="middle">WITH</text>
  <text class="tagline" x="457.5" y="384" text-anchor="middle">FOOD</text>

  <!-- brand disc -->
  <circle class="brand-disc" cx="457" cy="622" r="118"/>
  <circle class="brand-dot" cx="457" cy="585" r="14"/>
  <text class="brand-name" x="457" y="655" text-anchor="middle">Varenna</text>

  <!-- product windows -->
  <rect class="window" role="img" aria-label="Window showing white mould-coated salami sticks"
        fill="url(#salamiTone)" x="117" y="625" width="176" height="300" rx="16"/>
  <rect class="window" role="img" aria-label="Window showing white mould-coated salami sticks"
        fill="url(#salamiTone)" x="620" y="625" width="177" height="300" rx="16"/>

  <!-- product name label -->
  <path class="product-label-back"
        d="M346,784 C378,760 440,774 482,772 C545,768 590,790 584,830 C578,872 522,866 470,872 C418,876 352,876 338,844 C328,820 330,798 346,784 Z"/>
  <path class="product-label-front"
        d="M344,798 C368,780 430,788 470,786 C530,784 574,794 570,826 C566,858 518,860 468,860 C418,860 356,866 340,838 C332,822 332,808 344,798 Z"/>
  <text class="product-label" x="457" y="819" text-anchor="middle">HANDMADE</text>
  <text class="product-label" x="457" y="849" text-anchor="middle">SALAMI</text>

  <!-- bottom flap -->
  <rect class="panel" x="305" y="937" width="305" height="198"/>
  <g transform="translate(457 1036) rotate(-90)">
    <circle class="brand-dot" cx="-72" cy="0" r="7"/>
    <text class="flap-name" x="14" y="11" text-anchor="middle">Varenna</text>
  </g>
</svg>
</body>
</html>
```